Custom Apparel Decorating Company needs a Website Home Page Banner Design

We are in need of a website Home page banner design for a small company based in Canada called Quelvana. We are a custom apparel company that offers custom apparel (t-shirts, hoodies, hats etc) to Companies, Organizations/groups, bands, Spirit wear and individuals. We would like the design to match with the logo files we have attached to the campaign. The Website has not been created yet planning to tie the website into the home page banner for flow. Thinking of using Duda or Shopify for the website if that helps! We are really looking forward to seeing the designs.

Target Market(s)

Companies, Organizations/Groups, Bands, Spirit wear and Individuals. Anyone that is looking to have there company or own logo/Design put on a piece of clothing.

Requirements
Must have
• -Colours in the logo files.
• -FUN creating the Home Page Banner!!! :)
Nice to have
• -Up Beat feel to it (it's the first image you will see when you go to the website, it's the store front so we want to grab the attention of the potential customers)

```html
<!DOCTYPE html>
<html lang="en">
<head>
<meta charset="utf-8">
<title>Quelvana Apparel – Home Page Banners</title>
<link href="https://fonts.googleapis.com/css2?family=Montserrat:wght@400;500;600&family=Varela+Round&display=swap" rel="stylesheet">
<style>
  :root {
    --brand-blue: #3457a8;
    --brand-blue-deep: #2a4da6;
    --ink: #141414;
    --white: #ffffff;
    --page: #f1f1f1;
    --teal-light: #5f98ad;
    --teal-dark: #1f4a5c;
    --sky-light: #e9eef2;
    --rock-blue: #5a6a8c;
  }
  * { margin: 0; padding: 0; box-sizing: border-box; }
  html, body { width: 1200px; height: 2677px; overflow: hidden; }
  body {
    position: relative;
    background: var(--page);
    font-family: "Montserrat", sans-serif;
    color: var(--white);
  }
  .brand-name {
    font-family: "Montserrat", sans-serif;
    font-weight: 600;
    letter-spacing: 0.02em;
    white-space: nowrap;
  }
  .sheet-header {
    position: absolute; left: 0; top: 130px; width: 1200px;
    text-align: center;
  }
  .sheet-header .brand-name { font-size: 54px; color: var(--brand-blue); }

  .banner {
    position: absolute; overflow: hidden;
    box-shadow: 0 18px 40px rgba(0,0,0,0.28);
  }
  .photo { position: absolute; inset: 0; }
  .photo--wall {
    background:
      radial-gradient(ellipse 22% 60% at 50% 55%, #0d0f14 0%, #13161c 60%, rgba(19,22,28,0) 100%),
      radial-gradient(ellipse 30% 45% at 45% 30%, #9aa2a6 0%, rgba(154,162,166,0) 100%),
      linear-gradient(180deg, var(--teal-light) 0%, #3e7489 60%, #3a3a40 80%, #2a2a2e 100%);
  }
  .photo--pier {
    background:
      radial-gradient(ellipse 18% 55% at 78% 55%, #f4f4f6 0%, rgba(244,244,246,0) 100%),
      linear-gradient(180deg, #f7f8f9 0%, var(--sky-light) 25%, #8a9ab8 45%, var(--rock-blue) 70%, #6d6a80 100%);
  }
  .photo--friends {
    background:
      radial-gradient(ellipse 30% 60% at 40% 60%, #f2f2f2 0%, rgba(242,242,242,0) 100%),
      linear-gradient(180deg, #c9ccd3 0%, #8c97a8 50%, #6f86a8 100%);
  }

  .centre-block {
    position: absolute; left: 0; width: 100%; text-align: center;
  }
  .centre-block .brand-name { font-size: 24px; color: var(--white); display: block; }

  .btn {
    display: inline-block;
    border-radius: 22px;
    font-family: "Montserrat", sans-serif;
    font-weight: 500;
    font-size: 13px;
    letter-spacing: 0.18em;
    color: var(--white);
    text-align: center;
  }
  .btn--blue { background: var(--brand-blue-deep); width: 150px; height: 38px; line-height: 38px; }
  .btn--dark { background: var(--ink); }

  /* hero split banner */
  .hero-copy { position: absolute; left: 98px; top: 0; }
  .hero-copy .corner-mark { position: absolute; left: 0; top: 52px; font-size: 22px; color: var(--brand-blue); }
  .hero-copy h1 {
    position: absolute; left: -5px; top: 142px;
    font-family: "Varela Round", sans-serif;
    font-weight: 400; font-size: 56px; white-space: nowrap;
  }
  .hero-copy p {
    position: absolute; left: 0; top: 218px; width: 520px;
    font-size: 17px; line-height: 24px;
  }
  .hero-copy .btn--dark {
    position: absolute; left: 0; top: 286px;
    width: 178px; height: 42px; line-height: 42px; font-size: 15px;
  }

  /* split promo banner */
  .promo-panel {
    position: absolute; inset: 0;
    background: var(--brand-blue);
    clip-path: polygon(670px 0, 1050px 0, 1050px 450px, 470px 450px);
  }
  .promo-copy { position: absolute; right: 100px; top: 185px; text-align: right; }
  .promo-copy .brand-name { font-size: 22px; display: block; margin-bottom: 18px; }
  .promo-copy p { font-size: 17px; line-height: 27px; }
  .promo-copy .btn--dark {
    margin-top: 14px; width: 155px; height: 40px; line-height: 40px;
  }
</style>
</head>
<body>

  <header class="sheet-header">
    <span class="brand-name">Quelvana Apparel</span>
  </header>

  <!-- Desktop hero -->
  <section class="banner" style="left:130px; top:331px; width:940px; height:425px;">
    <div class="photo photo--wall" role="img" aria-label="Photo of a woman in a beanie and sunglasses wearing a black branded t-shirt in front of a blue graffiti wall"></div>
    <div class="centre-block" style="top:232px;">
      <span class="brand-name">Quelvana Apparel</span>
    </div>
    <div class="centre-block" style="top:280px;">
      <span class="btn btn--blue">SHOP NOW »</span>
    </div>
  </section>

  <!-- Split hero with headline -->
  <section class="banner" style="left:75px; top:1056px; width:1050px; height:450px;">
    <div class="photo photo--pier" role="img" aria-label="Photo of a woman in mirrored sunglasses and a white slogan t-shirt standing by the sea with blurred rocks behind"></div>
    <div class="hero-copy">
      <span class="brand-name corner-mark">Quelvana Apparel</span>
      <h1>Quelvana Apparel</h1>
      <p>Lorem ipsum dolor sit amet, consectetur adipiscing elit, sed do eiusmod tempor incididunt ut labore et dolore magna</p>
      <span class="btn btn--dark">SHOP NOW »</span>
    </div>
  </section>

  <!-- Full-width hero -->
  <section class="banner" style="left:75px; top:1578px; width:1050px; height:450px;">
    <div class="photo photo--wall" role="img" aria-label="Photo of a woman in a beanie and sunglasses wearing a black branded t-shirt in front of a blue graffiti wall"></div>
    <div class="centre-block" style="top:248px;">
      <span class="brand-name">Quelvana Apparel</span>
    </div>
    <div class="centre-block" style="top:296px;">
      <span class="btn btn--blue">SHOP NOW »</span>
    </div>
  </section>

  <!-- Split promo -->
  <section class="banner" style="left:75px; top:2099px; width:1050px; height:450px;">
    <div class="photo photo--friends" role="img" aria-label="Photo of two friends in caps and sunglasses wearing white printed t-shirts against a graffiti wall"></div>
    <div class="promo-panel"></div>
    <div class="promo-copy">
      <span class="brand-name">Quelvana Apparel</span>
      <p>Lorem ipsum dolor sit amet, consectetur<br>adipiscing elit, sed do</p>
      <span class="btn btn--dark">SHOP NOW »</span>
    </div>
  </section>

</body>
</html>
```